Business Cards for a Junk Removal Company

Hello,
We are looking to have business cards designed that are simple, bold, easy to read, and right to the point. Please see the attachments for our logo files. We want the card to be yellow on both sides ( Color code Yellow: #FFE01B). The logo text font is (Rockstar Extra Bold) and this is also in the files attached. Please make the text black for the logo. On the back side of the card, you can use white and black for text. Thank you in advance for your hard work!

Front of card-
Harbor Haul Away (logo)
Back of card-
Harbor Haul Away
Donate - Recycle - Dispose
555-271-8093
www.harborhaulaway.example
info@harborhaulaway.example

Industry/Entity Type

Junk removal

Contact Information for Business Card

FRONT OF CARD- Harbor Haul Away (logo) BACK OF CARD- Harbor Haul Away Donate - Recycle - Dispose 555-271-8093 www.harborhaulaway.example info@harborhaulaway.example

Font styles to use
Other font styles liked:
• Rockstar Extra Bold

Colors
FFF300
FFF600
FEFA6F
FFFEC7
FFFEE8

Requirements
Must have
• Must have color code Yellow: #FFE01B for the background of front and back of the card

```html
<!DOCTYPE html>
<html lang="en">
<head>
<meta charset="utf-8">
<title>Harbor Haul Away — Business Cards</title>
<link rel="stylesheet" href="https://fonts.googleapis.com/css2?family=Russo+One&family=Open+Sans:wght@400;600&display=swap">
<style>
  :root {
    --card-yellow: #EDD03F;
    --ink: #111111;
    --backdrop: #2f2927;
  }
  * { box-sizing: border-box; margin: 0; padding: 0; }
  html, body { width: 1200px; height: 716px; overflow: hidden; }
  body {
    background: var(--backdrop);
    display: flex;
    align-items: center;
    justify-content: center;
    gap: 60px;
    font-family: "Open Sans", sans-serif;
    color: var(--ink);
  }
  .card {
    position: relative;
    width: 520px;
    height: 297px;
    background: var(--card-yellow);
    overflow: hidden;
  }
  .wordmark {
    font-family: "Russo One", sans-serif;
    color: var(--ink);
    text-transform: uppercase;
    line-height: 0.95;
  }
  .card-front {
    display: flex;
    align-items: center;
    justify-content: center;
  }
  .card-front .wordmark { font-size: 52px; text-align: center; }
  .card-back .brand {
    position: absolute;
    left: 128px;
    top: 30px;
  }
  .card-back .wordmark { font-size: 34px; }
  .tagline {
    margin-top: 8px;
    font-family: "Russo One", sans-serif;
    font-size: 11px;
    letter-spacing: 0.3px;
    text-transform: uppercase;
  }
  .divider {
    position: absolute;
    left: 96px;
    right: 28px;
    top: 166px;
    height: 1px;
    background: var(--ink);
  }
  .contact-list {
    position: absolute;
    left: 28px;
    top: 190px;
    list-style: none;
    font-size: 12px;
    line-height: 20px;
  }
  .contact-list li { display: flex; align-items: center; gap: 8px; }
  .contact-list svg { width: 11px; height: 11px; flex: none; }
  .person {
    position: absolute;
    right: 44px;
    top: 128px;
    text-align: right;
  }
  .person-name {
    font-family: "Russo One", sans-serif;
    font-size: 20px;
    text-transform: uppercase;
    letter-spacing: 0.5px;
  }
  .person-title {
    font-size: 11px;
    font-weight: 600;
    text-transform: uppercase;
    letter-spacing: 0.5px;
  }
  .edge-tab {
    position: absolute;
    right: 0;
    top: 150px;
    width: 7px;
    height: 28px;
    background: var(--ink);
  }
</style>
</head>
<body>
  <section class="card card-front" aria-label="Card front">
    <div class="wordmark">Harbor<br>Haul Away</div>
  </section>

  <section class="card card-back" aria-label="Card back">
    <div class="brand">
      <div class="wordmark">Harbor<br>Haul Away</div>
      <p class="tagline">Donate - Recycle - Dispose</p>
    </div>

    <div class="divider"></div>

    <div class="person">
      <p class="person-name">Daniel Reyes</p>
      <p class="person-title">Director</p>
    </div>
    <div class="edge-tab"></div>

    <ul class="contact-list">
      <li>
        <svg viewBox="0 0 24 24" aria-hidden="true"><path fill="currentColor" d="M6.6 10.8a15 15 0 0 0 6.6 6.6l2.2-2.2a1 1 0 0 1 1-.25 11.4 11.4 0 0 0 3.6.57 1 1 0 0 1 1 1V20a1 1 0 0 1-1 1A17 17 0 0 1 3 4a1 1 0 0 1 1-1h3.5a1 1 0 0 1 1 1c0 1.25.2 2.46.57 3.6a1 1 0 0 1-.25 1z"/></svg>
        555-271-8093
      </li>
      <li>
        <svg viewBox="0 0 24 24" aria-hidden="true"><rect x="2.5" y="5" width="19" height="14" fill="none" stroke="currentColor" stroke-width="2"/><path d="M3 6l9 7 9-7" fill="none" stroke="currentColor" stroke-width="2"/></svg>
        info@harborhaulaway.example
      </li>
      <li>
        <svg viewBox="0 0 24 24" aria-hidden="true"><circle cx="12" cy="12" r="9.5" fill="none" stroke="currentColor" stroke-width="2"/><path d="M2.5 12h19M12 2.5c3 3 3 16 0 19M12 2.5c-3 3-3 16 0 19" fill="none" stroke="currentColor" stroke-width="1.6"/></svg>
        www.harborhaulaway.example
      </li>
    </ul>
  </section>
</body>
</html>
```